Life Insurance Landing Page (for lead gen)

We need a high converting life insurance page created. It will be housed at www.CoverageVerifyHub.com. We will be driving former life insurance prospects to this page where they will only need to confirm their phone number & email in order to receive an updated quote.
Updates

Only the page design is required, the coding will be done on our end. 

Target Market(s)

People who have expressed an interest in obtaining life insurance.

Industry/Entity Type

Life Insurance

Requirements
Must have
• 1) Under "CoverageVerifyHub.com" Please include a "Powered by KRBT" tag and match the colors of this site: http://thekrbt.com/life-insurance-services.html to the page.

2) The form should ask for their phone number and include an appointment calendar widget (we'll code the functionality) so they can choose the date/time of their call. It should also have an email confirmation field.

3) the overall message next to the form fields should be "Thanks for visiting Gordon (we'll personalize this "firstname" field ), please let us know the best time to schedule a brief call so we can give you an updated, rock bottom pricing quote on a policy. We'll also email you with the information, please confirm your email here and we'll send you the details.

4) We'd like to include a box that appears to be a personalized "quote briefing" snapshot that will list this information: "Name: _________" "Birth Date:"____________" "Policy Type: _______", "Coverage Amount: ____________" " all these fields will be populated into the page.

```html
<!DOCTYPE html>
<html lang="en">
<head>
<meta charset="utf-8">
<title>CoverageVerifyHub.com – Affordable Life Insurance</title>
<link href="https://fonts.googleapis.com/css2?family=Fredoka:wght@500;600&family=Open+Sans:ital,wght@0,400;0,600;0,700;1,400&display=swap" rel="stylesheet">
<style>
:root{
  --orange:#e8790f;
  --orange-deep:#d95d00;
  --orange-light:#ffc21c;
  --gold-text:#b9a16a;
  --text:#6b6b6b;
  --text-dark:#333;
  --page:#fafbfb;
  --band:#ececec;
  --line:#d6d6d6;
  --social:#1e5b93;
  --social-light:#2d9ed9;
}
*{margin:0;padding:0;box-sizing:border-box}
html,body{width:1024px;height:1200px;overflow:hidden;background:var(--page)}
body{font-family:"Open Sans",Arial,sans-serif;color:var(--text)}
.page{position:relative;width:1024px;height:1200px;overflow:hidden;background:var(--page)}
.abs{position:absolute}
h2,.display{font-family:"Fredoka","Open Sans",sans-serif;font-weight:600;color:var(--orange)}

/* header */
.hero-bg{left:0;top:0;width:1024px;height:440px}
.logo{left:135px;top:12px;font-size:20px;font-weight:600;color:var(--orange);letter-spacing:-.3px}
.powered{left:136px;top:40px;font-size:10px;font-weight:600;color:#888;letter-spacing:.3px}
.powered b{color:var(--social)}
.social-top{left:584px;top:17px;display:flex;gap:10px}
.social-top span{width:18px;height:18px;border-radius:50%;background:var(--social)}
.social-top span:nth-child(2){background:var(--social-light)}
.call{left:676px;top:17px;display:flex;align-items:center;gap:6px;font-size:13.5px;font-weight:600;color:#888}
.call b{color:var(--orange-deep)}
.call .phone-icon{width:18px;height:18px;background:var(--social);border-radius:3px;display:flex;align-items:center;justify-content:center}

/* hero */
.hero-title{left:430px;top:80px;width:536px;text-align:center;font-size:26px}
.hero-sub{left:430px;top:111px;width:536px;text-align:center;font-size:14px;color:var(--gold-text)}
.hero-photo{left:432px;top:145px;width:228px;height:262px;border-radius:46% 46% 26% 26%/34% 34% 14% 14%;
  background:linear-gradient(100deg,#e6c79b 0%,#7d9bb7 40%,#8e8c92 70%,#8fcde8 100%);opacity:.85}

.panel{background:#fff;border:1px solid var(--line);border-radius:4px;box-shadow:0 2px 4px rgba(0,0,0,.08)}
.panel-head{height:24px;padding:0 10px;background:linear-gradient(#ffc21c,#e97a05);color:#fff;font-family:"Fredoka","Open Sans",sans-serif;font-weight:600;font-size:13px;line-height:24px;border-radius:3px 3px 0 0}

.briefing{left:676px;top:146px;width:290px;height:114px}
.briefing dl{padding:6px 12px 0}
.briefing .row{display:flex;align-items:flex-end;height:20px;font-size:10.5px}
.briefing dt{font-weight:700;color:var(--text-dark);white-space:nowrap;margin-right:6px}
.briefing dd{flex:1;border-bottom:1px solid #bbb;height:13px}

.calendar{left:676px;top:268px;width:290px;height:146px}
.cal-body{display:flex;padding:6px 8px 0}
.cal-month{font-size:10px;font-weight:700;color:var(--text-dark);display:flex;justify-content:space-between;width:154px;margin-bottom:3px}
.cal-month span{color:var(--orange)}
.cal-grid{display:grid;grid-template-columns:repeat(7,22px);grid-auto-rows:15px;font-size:9px;text-align:center;line-height:15px;color:#555}
.cal-grid .dow{font-weight:700;color:#999}
.cal-grid .sel{background:var(--orange);color:#fff;border-radius:2px;font-weight:700}
.times{margin-left:10px;border-left:1px solid #eee;padding-left:10px;width:104px}
.times p{font-size:9.5px;font-weight:700;color:var(--text-dark);margin-bottom:4px}
.slot{height:17px;margin-bottom:3px;border:1px solid var(--line);border-radius:2px;font-size:9.5px;text-align:center;line-height:15px;color:#555}
.slot.sel{background:var(--orange);border-color:var(--orange-deep);color:#fff;font-weight:700}

/* quote form */
.quote-card{left:126px;top:77px;width:278px;height:360px}
.quote-title{left:126px;top:93px;width:276px;text-align:center;font-family:"Fredoka","Open Sans",sans-serif;font-size:23px;line-height:27px;color:#fff;font-weight:600;letter-spacing:-.3px;text-shadow:0 1px 2px rgba(150,60,0,.5)}
.form-message{left:140px;top:172px;width:250px;font-size:9.5px;line-height:12.5px;color:#555;text-align:center}
.form-message b{color:var(--orange-deep)}
.field{left:144px;width:241px;height:30px;border:1px solid #bcbcbc;border-radius:3px;background:#fff;font-size:10.5px;color:#555;padding:7px 13px;box-shadow:inset 0 1px 2px rgba(0,0,0,.08)}
.field i{color:#c00;font-style:normal}
.submit{left:184px;top:346px;width:161px;height:38px;border:1px solid #c46a00;border-radius:2px;background:linear-gradient(#ffc21c,#ef8e06);color:#fff;font-size:17px;font-weight:600;text-align:center;line-height:36px;font-family:"Fredoka","Open Sans",sans-serif;text-shadow:0 1px 2px rgba(150,60,0,.5)}

/* content */
.section-h{font-size:22px}
.about-photo{left:136px;top:520px;width:108px;height:108px;border-radius:50%;background:radial-gradient(circle at 50% 40%,#d6e6f4,#9fbbd6)}
.about-text{left:258px;top:516px;width:246px;font-size:13px;line-height:19.2px}
.about-more{left:140px;top:645px;width:370px;font-size:13px;line-height:19.2px}
.list{list-style:none;font-size:13.3px}
.list li{height:25.6px;display:flex;align-items:center;gap:15px}
.list li::before{content:"";width:0;height:0;border-left:5px solid #666;border-top:4px solid transparent;border-bottom:4px solid transparent}
.benefits{left:522px;top:513px}
.offers{left:716px;top:513px;font-weight:700;color:#757575}
.family-photo{left:132px;top:720px;width:368px;height:138px;background:linear-gradient(90deg,#b5a897 0%,#e3c4a5 35%,#c9a88d 55%,#cfdbe6 80%,#bcd3e6 100%)}
.family-text{left:519px;top:725px;width:370px;font-size:13px;line-height:19.2px}

/* testimonials */
.testimonial{top:930px;width:240px}
.avatar{width:70px;height:70px;border-radius:50%;background:linear-gradient(#9a8f86,#5a534f)}
.t-name{position:absolute;left:86px;top:21px;font-size:12.5px;font-weight:700;color:var(--text-dark)}
.t-org{position:absolute;left:87px;top:41px;font-size:10px;font-style:italic;color:#777}
.t-quote{margin-top:16px;font-size:10px;line-height:16px;color:#555;width:240px}

/* cta band */
.band{left:0;top:1085px;width:1024px;height:71px;background:var(--band)}
.band-title{left:196px;top:1100px;font-size:20px;color:#666}
.band-title b{color:#ff6a13;font-weight:600}
.band-sub{left:197px;top:1124px;font-size:12px;color:#777;letter-spacing:.2px}
.band-btn{left:648px;top:1101px;width:160px;height:40px;border-radius:3px;border:1px solid #c46a00;background:linear-gradient(#ffb21c,#ec7f06);color:#fff;font-weight:700;font-size:13.5px;text-align:center;line-height:38px;box-shadow:0 2px 3px rgba(0,0,0,.2)}

.footer{left:125px;top:1171px;font-size:9.8px;color:#777}
.social-foot{left:811px;top:1167px;display:flex;gap:7px}
.social-foot span{width:20px;height:20px;background:var(--social);box-shadow:0 1px 2px rgba(0,0,0,.3)}
.social-foot span:nth-child(2){background:var(--social-light)}
</style>
</head>
<body>
<div class="page">

  <svg class="abs hero-bg" viewBox="0 0 1024 440" aria-hidden="true">
    <defs>
      <linearGradient id="heroGrad" x1="0" y1="0" x2="0" y2="1">
        <stop offset="0" stop-color="#ffffff"/>
        <stop offset="1" stop-color="#e6ecf7"/>
      </linearGradient>
    </defs>
    <path d="M0 0H1024V418Q512 392 0 432Z" fill="url(#heroGrad)"/>
  </svg>

  <header>
    <div class="abs logo">CoverageVerifyHub.com</div>
    <div class="abs powered">Powered by <b>KRBT</b></div>
    <div class="abs social-top" aria-hidden="true"><span></span><span></span><span></span></div>
    <div class="abs call">
      <span class="phone-icon"><svg width="11" height="11" viewBox="0 0 24 24"><path fill="#fff" d="M6.6 10.8a15 15 0 0 0 6.6 6.6l2.2-2.2c.3-.3.7-.4 1-.2 1.1.4 2.3.6 3.6.6.6 0 1 .4 1 1V20c0 .6-.4 1-1 1A17 17 0 0 1 3 4c0-.6.4-1 1-1h3.5c.6 0 1 .4 1 1 0 1.3.2 2.5.6 3.6.1.3 0 .7-.2 1z"/></svg></span>
      Call us today <b>+1800.555.0147</b>
    </div>
  </header>

  <h1 class="abs display hero-title">Get Affordable Life Insurance</h1>
  <p class="abs hero-sub">Provide Security to your loved ones for years to come</p>
  <div class="abs hero-photo" role="img" aria-label="Smiling family lying together on the floor"></div>

  <section class="abs panel briefing" aria-label="Quote briefing">
    <div class="panel-head">Your Quote Briefing</div>
    <dl>
      <div class="row"><dt>Name:</dt><dd></dd></div>
      <div class="row"><dt>Birth Date:</dt><dd></dd></div>
      <div class="row"><dt>Policy Type:</dt><dd></dd></div>
      <div class="row"><dt>Coverage Amount:</dt><dd></dd></div>
    </dl>
  </section>

  <section class="abs panel calendar" aria-label="Schedule your call">
    <div class="panel-head">Choose the Date &amp; Time of Your Call</div>
    <div class="cal-body">
      <div>
        <div class="cal-month"><span>&lsaquo;</span>June 2025<span>&rsaquo;</span></div>
        <div class="cal-grid">
          <span class="dow">S</span><span class="dow">M</span><span class="dow">T</span><span class="dow">W</span><span class="dow">T</span><span class="dow">F</span><span class="dow">S</span>
          <span>1</span><span>2</span><span>3</span><span>4</span><span>5</span><span>6</span><span>7</span>
          <span>8</span><span>9</span><span>10</span><span>11</span><span class="sel">12</span><span>13</span><span>14</span>
          <span>15</span><span>16</span><span>17</span><span>18</span><span>19</span><span>20</span><span>21</span>
          <span>22</span><span>23</span><span>24</span><span>25</span><span>26</span><span>27</span><span>28</span>
          <span>29</span><span>30</span>
        </div>
      </div>
      <div class="times">
        <p>Available times</p>
        <div class="slot">9:00 AM</div>
        <div class="slot sel">11:00 AM</div>
        <div class="slot">1:30 PM</div>
        <div class="slot">4:00 PM</div>
      </div>
    </div>
  </section>

  <svg class="abs quote-card" viewBox="0 0 278 360" aria-hidden="true">
    <defs>
      <linearGradient id="cardGrad" x1="0" y1="0" x2="0" y2="1">
        <stop offset="0" stop-color="#ececec"/><stop offset=".5" stop-color="#fdfdfd"/><stop offset="1" stop-color="#f0f0f0"/>
      </linearGradient>
      <linearGradient id="headGrad" x1="0" y1="0" x2="0" y2="1">
        <stop offset="0" stop-color="#ffc21c"/><stop offset="1" stop-color="#de6500"/>
      </linearGradient>
    </defs>
    <path d="M4 8H278V340L138 358L4 340Z" fill="#d8d8d8"/>
    <path d="M0 4H274V336L138 354L0 336Z" fill="url(#cardGrad)"/>
    <path d="M0 6Q0 0 6 0H268Q274 0 274 6V60L138 88L0 60Z" fill="url(#headGrad)"/>
  </svg>
  <div class="abs quote-title">GET A QUOTATION<br>FOR FREE!</div>
  <p class="abs form-message"><b>Thanks for visiting Gordon,</b> please let us know the best time to schedule a brief call so we can give you an updated, rock bottom pricing quote on a policy. We’ll also email you with the information, please confirm your email here and we’ll send you the details.</p>
  <div class="abs field" style="top:266px">Phone Number<i>*</i></div>
  <div class="abs field" style="top:304px">Confirm Email<i>*</i></div>
  <div class="abs submit">SUBMIT NOW</div>

  <h2 class="abs section-h" style="left:133px;top:464px">About Life Insurance</h2>
  <h2 class="abs section-h" style="left:518px;top:464px">Key Benefits</h2>
  <h2 class="abs section-h" style="left:712px;top:464px">What We Offer</h2>

  <div class="abs about-photo" role="img" aria-label="Family portrait in a circular frame"></div>
  <p class="abs about-text">Lid est laborum dolo rumes fugats untras. Etharums ser quidem rerum faci­lis dolores nemis omnis fugats vitaes nemo minima rerums unsers sadips amets. Lid est laborum dolo rumes fugats untras.</p>
  <p class="abs about-more">Etharums ser quidem rerum facilis dolores nemis omnis fugats vitaes nemo minima rerums unsers sadips amets.</p>

  <ul class="abs list benefits">
    <li>Lid est laborum</li><li>dolo rumes fugats</li><li>Etharums ser quidem</li><li>Rerum facilis dolores</li><li>Nemis omnis fugats</li><li>Vitaes nemo minima</li><li>Rerums unsers sadips</li>
  </ul>
  <ul class="abs list offers">
    <li>Auto Insurance</li><li>Home Insurance</li><li>Life Insurance</li><li>Health Insurance</li><li>Business Insurance</li><li>Restaurant Insurance</li><li>Workers Comp</li>
  </ul>

  <div class="abs family-photo" role="img" aria-label="Close-up of a happy family against a blue sky"></div>
  <p class="abs family-text">Lid est laborum dolo rumes fugats untras. Etharums ser quidem rerum facilis dolores nemis omnis fugats vitaes nemo minima rerums unsers sadips amets. Lid est laborum dolo rumes fugats untras. Etharums ser quidem rerum facilis dolores nemis omnis fugats vitaes nemo minima rerums unsers sadips amets.</p>

  <h2 class="abs section-h" style="left:134px;top:886px">Client Testimonials</h2>

  <div class="abs testimonial" style="left:134px">
    <div class="avatar" role="img" aria-label="Portrait of client"></div>
    <div class="t-name">Marcus Dale</div><div class="t-org">Bramble Agency</div>
    <p class="t-quote">“Lorem ipsum dolor sit amet, consectetur adipisic­ing elit, sed do eiusmod tempor incididunt ut labore et dolore magna aliqua.”</p>
  </div>
  <div class="abs testimonial" style="left:391px">
    <div class="avatar" role="img" aria-label="Portrait of client"></div>
    <div class="t-name">Nadia Rowe</div><div class="t-org">Kestrel Corp</div>
    <p class="t-quote">“Lorem ipsum dolor sit amet, consectetur adipisic­ing elit, sed do eiusmod tempor incididunt ut labore et dolore magna aliqua.”</p>
  </div>
  <div class="abs testimonial" style="left:647px">
    <div class="avatar" role="img" aria-label="Portrait of client" style="background:linear-gradient(#d9d2cc,#8a7e76)"></div>
    <div class="t-name">Owen Hart</div><div class="t-org">Harbor Outsource</div>
    <p class="t-quote">“Lorem ipsum dolor sit amet, consectetur adipisic­ing elit, sed do eiusmod tempor incididunt ut labore et dolore magna aliqua.”</p>
  </div>

  <div class="abs band"></div>
  <div class="abs band-title">Get started today <b>+1800.555.0147</b></div>
  <div class="abs band-sub">If you have any further queries please do not hesitate to contact us.</div>
  <div class="abs band-btn">Request a Quote</div>

  <footer>
    <div class="abs footer">Copyright 2014 CoverageVerifyHub.com &nbsp;|&nbsp; All Rights Reserved</div>
    <div class="abs social-foot" aria-hidden="true"><span></span><span></span><span></span></div>
  </footer>
</div>
</body>
</html>
```